Email Marketing for HR and Career Consulting Company

I am looking for a email marketing template that will be developed in HTML format. Right now, we need PSD file format.

The content will include:

1. Featured / Poplar Blog post
2. Latest blog post this week
3. Latest jobs this week
4. Connect with us (social media)

This is a bi-weekly template which we will be sending to people who sign up our weekly newsletter. The purpose of the newsletter is to provide career advise and also latest jobs that's available from our company so that we can redirect them to our career page or apply to our latest jobs.
Updates

Project Deadline Extended
Reason: I am extending this deadline as I would like to see more designs. So far, I have only shortlisted one design that is close to what I am looking for. To all designers, please note that your design would have to be practical and easy to navigate. It also must take into consideration that when we develop this into html, it will b responsive.

Target Market(s)

Job seekers - age group 25 - 45

Industry/Entity Type

Consulting

Font styles to use
Other font styles liked:
• Helvetical

Colors
0492cd
e34197
ec1f27
85cae6
33a6d7
85acd3
eda3c7
e667a6
f59195

Requirements
Must have
• 1. Social media icons
• 2. Links - jobs, contact us
• 3. Popular career advice
• 4. Latest career advice
• 5. Featured jobs
• 6. Popular jobs
Nice to have
• I would like to see clean and minimalist design. Please try to avoid black color. Use pastel colors as much as possible. Our website is www.careerplume.com.sg
Should not have
• Should avoid black and dark colors

```html
<!DOCTYPE html>
<html lang="en">
<head>
<meta charset="utf-8">
<title>Careerplume Weekly Newsletter</title>
<link rel="stylesheet" href="https://fonts.googleapis.com/css2?family=Arimo:wght@400;700&display=swap">
<style>
:root{
  --page:#f4f2f2;
  --blue:#29a3dc;
  --blue-deep:#1f8fc6;
  --ink:#2f3337;
  --ink-soft:#55595d;
  --white:#ffffff;
  --pink:#ec1f27;
}
*{margin:0;padding:0;box-sizing:border-box}
html,body{width:1200px;height:3586px;overflow:hidden}
body{background:var(--page);font-family:"Arimo",Helvetica,Arial,sans-serif;color:var(--ink);position:relative}
.abs{position:absolute}
a{color:inherit}

.preheader{top:26px;left:163px;width:870px;font-size:14px;color:var(--ink-soft);display:flex;justify-content:space-between}
.preheader a{color:var(--blue-deep)}

.masthead{top:60px;left:163px;width:870px;height:76px;background:var(--blue);display:flex;align-items:center;justify-content:space-between;padding:0 28px 0 24px;color:var(--white)}
.brand{font-size:42px;font-weight:400;letter-spacing:-0.5px}
.nav{display:flex;gap:26px;font-size:22px}

.issue-row{top:152px;left:163px;width:870px;display:flex;justify-content:space-between;align-items:center}
.issue{font-size:15px;color:var(--blue);letter-spacing:.3px}
.social{display:flex;gap:8px}
.social span{width:22px;height:22px;border-radius:50%;background:var(--blue-deep);display:block}

.section-rule{left:163px;width:870px;height:2px;background:var(--blue)}
.tab{height:34px;background:var(--blue);color:var(--white);font-size:20px;line-height:34px;padding:0 14px;white-space:nowrap}

.photo{border-radius:2px}
.post-title{font-size:21px;line-height:28px;font-weight:400;color:var(--ink);width:420px}
.post-text{font-size:15.5px;line-height:26px;color:var(--ink-soft);width:420px}
.btn{background:var(--blue);color:var(--white);font-size:15px;font-weight:700;text-align:center;border-radius:3px;height:36px;line-height:36px;width:105px}
.btn-wide{background:var(--blue);color:var(--white);font-size:16px;text-align:center;border-radius:3px;width:182px;height:46px;line-height:46px}

.job{left:186px;width:818px;height:81px}
.job-title{font-size:21px;color:var(--ink)}
.job-meta{margin-top:12px;font-size:16px;color:var(--ink-soft);display:flex}
.job-meta span:nth-child(1){width:132px}
.job-meta span:nth-child(2){width:190px}
.apply{position:absolute;right:0;top:14px;width:160px;height:22px;line-height:22px;background:var(--blue);color:var(--white);font-size:12px;font-weight:700;text-align:center;letter-spacing:.2px}

.stay{top:3372px;left:186px;font-size:20px;color:var(--blue)}
.stay-social{top:3370px;left:841px}

.footer{top:3416px;left:163px;width:870px;height:127px;background:var(--blue);color:var(--white)}
.footer-mark{position:absolute;left:62px;top:16px;width:95px;height:95px;border-radius:50%;background:var(--white)}
.footer-text{position:absolute;left:193px;top:25px;font-size:15px;line-height:27px}
.footer-text .unsub{color:var(--pink)}
</style>
</head>
<body>

<div class="abs preheader">
  <span>Having trouble viewing this email? <a href="#">View it in your browser</a></span>
  <a href="#">Forward to a Friend</a>
</div>

<header class="abs masthead">
  <div class="brand">careerplume</div>
  <nav class="nav"><span>JOBS</span><span>CONTACT US</span></nav>
</header>

<div class="abs issue-row">
  <span class="issue">WEEKLY NEWSLETTER - AUGUST 30,2016</span>
  <div class="social"><span></span><span></span><span></span><span></span><span></span><span></span></div>
</div>

<!-- Popular career advice -->
<div class="abs tab" style="top:201px;left:163px;width:287px">POPULAR CAREER ADVICE</div>
<div class="abs section-rule" style="top:233px"></div>

<div class="abs photo" role="img" aria-label="Man in a suit adjusting his tie" style="top:294px;left:163px;width:390px;height:282px;background:linear-gradient(135deg,#2b2523,#6b5a4e 55%,#2c2826)"></div>
<h2 class="abs post-title" style="top:337px;left:595px">The Interview Process, Part 2: Inside the Interviewer's Playbook</h2>
<p class="abs post-text" style="top:424px;left:595px">Today, we will be focusing on that mysterious, perhaps at times intimidating, character that is the interviewer. Everyone can benefit from getting a quick look inside the typical interviewer's mind ...</p>
<div class="abs btn" style="top:544px;left:597px">Read More</div>

<h2 class="abs post-title" style="top:716px;left:163px">Always Be Employed</h2>
<p class="abs post-text" style="top:771px;left:163px;width:430px">The best way to get a job is to have a job". This is" .something that gets reiterated time and time again A sentence that implies, right from the very beginning, that unemployed job ...</p>
<div class="abs btn" style="top:898px;left:492px">Read More</div>
<div class="abs photo" role="img" aria-label="Colleagues arranging sticky notes on a glass wall" style="top:650px;left:641px;width:392px;height:282px;background:linear-gradient(135deg,#dfe6ea,#b9cfd6 45%,#e8e3d6)"></div>

<div class="abs btn-wide" style="top:1013px;left:504px">VIEW ALL ADVICE</div>

<!-- Latest career advice -->
<div class="abs tab" style="top:1133px;left:767px;width:266px">LATEST CAREER ADVICE</div>
<div class="abs section-rule" style="top:1165px"></div>

<div class="abs photo" role="img" aria-label="Hand holding a tablet showing a job search screen" style="top:1248px;left:163px;width:390px;height:282px;background:linear-gradient(135deg,#3f79a4,#9cc3dc 55%,#e3eef4)"></div>
<h2 class="abs post-title" style="top:1272px;left:595px">Contract Jobs: Can They Really Be A Career Option?</h2>
<p class="abs post-text" style="top:1357px;left:595px">Making a career out of contract jobs isn't out of the realm of possibility. While it does involve a lot of work, .the payoff, the joy of entrepreneurship, is hard to match .But where to start? How do you keep it going? ...</p>
<div class="abs btn" style="top:1478px;left:597px">Read More</div>

<h2 class="abs post-title" style="top:1625px;left:163px">Things to Expect After You have Quit 10 Your Job</h2>
<p class="abs post-text" style="top:1707px;left:163px;width:430px">Congratulations! You have just quit your job and you are taking a well-deserved break. There are a lot of reasons why someone would quit a job. It can be because of a lack of interest, change of career path or simply that you need to take time off ...</p>
<div class="abs btn" style="top:1860px;left:165px">Read More</div>
<div class="abs photo" role="img" aria-label="Cartoon character with a speech bubble saying goodbye" style="top:1614px;left:641px;width:392px;height:282px;background:linear-gradient(135deg,#a9d2dc,#c9e4e9 60%,#e9e1d4)"></div>

<!-- Featured jobs -->
<div class="abs tab" style="top:1955px;left:163px;width:196px">FEATURED JOBS</div>
<div class="abs section-rule" style="top:1987px"></div>

<div class="abs job" style="top:2041px"><div class="job-title">Senior / Recruitment Consultant - Executive Search Division</div><div class="job-meta"><span>Singapore</span><span>Human Resource</span><span>Full-time</span></div><div class="apply">APPLY FOR THIS JOB</div></div>
<div class="abs job" style="top:2122px"><div class="job-title">TMS Support Analyst, APAC</div><div class="job-meta"><span>Singapore</span><span>Information Technology</span><span>Full-time</span></div><div class="apply">APPLY FOR THIS JOB</div></div>
<div class="abs job" style="top:2203px"><div class="job-title">Logistics Manager - Fashion Retail</div><div class="job-meta"><span>Singapore</span><span>Logistigs</span><span>Full-time</span></div><div class="apply">APPLY FOR THIS JOB</div></div>
<div class="abs job" style="top:2284px"><div class="job-title">Manager, Business Process Improvement, APAC</div><div class="job-meta"><span>Singapore</span><span>Supply Chain</span><span>Full-time</span></div><div class="apply">APPLY FOR THIS JOB</div></div>
<div class="abs job" style="top:2365px"><div class="job-title">Manager, Trade Compliance, Service Logistic, APAC</div><div class="job-meta"><span>Singapore</span><span>Supply Chain</span><span>Full-time</span></div><div class="apply">APPLY FOR THIS JOB</div></div>

<div class="abs btn-wide" style="top:2531px;left:504px">VIEW ALL JOBS</div>

<!-- Popular jobs -->
<div class="abs tab" style="top:2648px;left:846px;width:187px">POPULAR JOBS</div>
<div class="abs section-rule" style="top:2680px"></div>

<div class="abs job" style="top:2734px"><div class="job-title">Senior / Recruitment Consultant - Executive Search Division</div><div class="job-meta"><span>Singapore</span><span>Human Resource</span><span>Full-time</span></div><div class="apply">APPLY FOR THIS JOB</div></div>
<div class="abs job" style="top:2815px"><div class="job-title">TMS Support Analyst, APAC</div><div class="job-meta"><span>Singapore</span><span>Information Technology</span><span>Full-time</span></div><div class="apply">APPLY FOR THIS JOB</div></div>
<div class="abs job" style="top:2896px"><div class="job-title">Logistics Manager - Fashion Retail</div><div class="job-meta"><span>Singapore</span><span>Logistigs</span><span>Full-time</span></div><div class="apply">APPLY FOR THIS JOB</div></div>
<div class="abs job" style="top:2977px"><div class="job-title">Manager, Business Process Improvement, APAC</div><div class="job-meta"><span>Singapore</span><span>Supply Chain</span><span>Full-time</span></div><div class="apply">APPLY FOR THIS JOB</div></div>
<div class="abs job" style="top:3058px"><div class="job-title">Manager, Trade Compliance, Service Logistic, APAC</div><div class="job-meta"><span>Singapore</span><span>Supply Chain</span><span>Full-time</span></div><div class="apply">APPLY FOR THIS JOB</div></div>

<div class="abs btn-wide" style="top:3225px;left:504px">VIEW ALL JOBS</div>

<!-- Stay connected -->
<div class="abs stay">STAY CONNECTED</div>
<div class="abs social stay-social"><span></span><span></span><span></span><span></span><span></span><span></span></div>

<footer class="abs footer">
  <div class="footer-mark"></div>
  <div class="footer-text">
    This newsletter was sent to reader@inboxmail.net &nbsp;because you are subscribed.<br>
    Rather not receive our newsletter anymore? &nbsp;<span class="unsub">Unsubscribe</span> instantly<br>
    Copyright ©2016 careerplume.com. All Rights Reserved.
  </div>
</footer>

</body>
</html>
```